Destination Wedding Photographer

I am a Wedding photographer based in San Juan, Puerto Rico. The banner will be shown in the United States to brides that plan to have their wedding in Puerto Rico.

I want to highlight the following words/phrases
Puerto Rico
Destination Wedding
Photographer
(in that order)

feel free to get creative adding your own inspired text.

My web site: www.benitolavarro.com

Target Market(s)

Brides in the united states looking for a photographer for their wedding in Puerto Rico

Industry/Entity Type

Wedding

Requirements
Must have
• + Your ad must be a .gif, .png or .jpg smaller than 40kb in filesize
+ include the following sizes: 300x250, 728x90, 160x600, 468x60, or 120x600
+ Your ad must include the advertiser's brand
+ Your ad must have a border
Should not have
• + Your ad cannot imitate computer effects like scrolling or mousing over
+ No animations longer than 30 seconds
+ No strobe or flashing effects allowed
+ Your ad and campaign must not feature or promote alcohol, anabolic steroids, drugs, financial products, gambling, adult content, or weight loss products

```html
<!DOCTYPE html>
<html lang="en">
<head>
<meta charset="utf-8">
<title>Benito Lavarro – Destination Wedding Photography</title>
<link rel="stylesheet" href="https://fonts.googleapis.com/css2?family=Advent+Pro:wght@200;300&family=Shadows+Into+Light+Two&display=swap">
<style>
  :root {
    --bg: #2b2b2b;
    --panel: #2d2d2d;
    --frame: #ffffff;
    --text: #ffffff;
    --muted: #d8d8d8;
  }
  * { margin: 0; padding: 0; box-sizing: border-box; }
  html, body { width: 1200px; height: 322px; overflow: hidden; background: var(--bg); }
  .banner {
    position: relative;
    width: 1200px;
    height: 322px;
    background: var(--bg);
    font-family: "Advent Pro", sans-serif;
    color: var(--text);
  }
  .banner__frame {
    position: absolute;
    left: 18px; top: 18px;
    width: 1164px; height: 286px;
    border: 6px solid var(--frame);
    background: var(--panel);
  }
  .brand {
    position: absolute;
    left: 72px; top: 64px;
    font-weight: 200;
    font-size: 36px;
    line-height: 1;
    letter-spacing: 1px;
    white-space: nowrap;
  }
  .headline {
    position: absolute;
    left: 372px; top: 60px;
    white-space: nowrap;
  }
  .headline__place {
    font-weight: 200;
    font-size: 45px;
    letter-spacing: -1px;
  }
  .script {
    font-family: "Shadows Into Light Two", cursive;
    font-weight: 400;
    color: var(--muted);
  }
  .headline__tagline { font-size: 19px; margin-left: 3px; }
  .pitch-line {
    position: absolute;
    right: 37px;
    text-align: right;
    white-space: nowrap;
  }
  .pitch__lead { font-size: 19px; line-height: 24px; }
  .pitch__big {
    font-weight: 200;
    font-size: 35px;
    line-height: 38px;
  }
  .pitch__lead--first { top: 44px; }
  .pitch__big--first { top: 76px; }
  .pitch__lead--second { top: 140px; }
  .pitch__big--second { top: 168px; }
  .contact {
    position: absolute;
    right: 37px;
    text-align: right;
    font-weight: 300;
    font-size: 17px;
    line-height: 22px;
    letter-spacing: 1px;
    color: var(--muted);
    text-transform: uppercase;
    white-space: nowrap;
  }
  .contact__phone { top: 234px; }
  .contact__web { top: 258px; }
  .gallery {
    position: absolute;
    left: 50px; top: 135px;
    display: flex;
    height: 140px;
  }
  .gallery__photo { height: 140px; }
  .photo--bride { width: 140px; background: radial-gradient(circle at 60% 55%, #6b4b3e, #1c1412 70%); }
  .photo--sunset { width: 213px; background: linear-gradient(180deg, #3f63a8 0%, #5a5f93 35%, #c77a6a 55%, #2a3a6a 75%, #0f1728 100%); }
  .photo--beach-couple { width: 140px; background: linear-gradient(180deg, #9fd6d6 0%, #c6e4e0 45%, #f1ede8 100%); }
  .photo--kiss { width: 140px; background: linear-gradient(90deg, #8a7a6c 0%, #3b2d25 50%, #1a1411 100%); }
  .photo--ceremony { width: 240px; background: linear-gradient(180deg, #8fc4e6 0%, #bfe0ef 40%, #e9e2d8 65%, #d9c6b3 100%); }
</style>
</head>
<body>
<div class="banner">
  <div class="banner__frame"></div>

  <div class="brand">Benito Lavarro</div>

  <div class="headline">
    <span class="headline__place">PUERTO RICO</span><span class="script headline__tagline">...the island of enchantment...</span>
  </div>

  <div class="pitch-line script pitch__lead pitch__lead--first">planning a</div>
  <div class="pitch-line pitch__big pitch__big--first">DESTINATION WEDDING?</div>
  <div class="pitch-line script pitch__lead pitch__lead--second">looking for professional</div>
  <div class="pitch-line pitch__big pitch__big--second">PHOTOGRAPHY?</div>

  <div class="contact contact__phone">787-555-0142</div>
  <div class="contact contact__web">www.benitolavarro.com/</div>

  <div class="gallery">
    <div class="gallery__photo photo--bride" role="img" aria-label="Close portrait of a bride looking down"></div>
    <div class="gallery__photo photo--sunset" role="img" aria-label="Couple silhouetted on coastal rocks under a dramatic sunset sky"></div>
    <div class="gallery__photo photo--beach-couple" role="img" aria-label="Bride with pink bouquet and groom embracing on the beach"></div>
    <div class="gallery__photo photo--kiss" role="img" aria-label="Bride in veil and groom about to kiss in soft light"></div>
    <div class="gallery__photo photo--ceremony" role="img" aria-label="Beach wedding ceremony under a white canopy with guests seated"></div>
  </div>
</div>
</body>
</html>
```